Letterhead and matching envelope design for a dental office

We need a new stationary design, letterhead and envelope #10, for a dental office in Denver area. We are called Brightfield Dental. We want a simple and minimalistic design but not a boring design. I wish to have one good point that makes it look professional. I have attached our logo. Feel free to use either one. I want the design for letterhead and envelope look like a "matching pair" but not look the same. The envelope doesn't have to be white and it will have an address window on bottom left.

Target Market(s)

everyone who visits dentist (adults)

Industry/Entity Type

Dental

Font styles to use
Other font styles liked:
• close to font on logo or something that matches well

Requirements
Must have
• professional
• simple, minimalistic
• unique point that stands out
Nice to have
• matching but not same design for letterhead and envelope
Should not have
• not look like all the other boring designs
• no flowery, distracting feats

```html
<!DOCTYPE html>
<html lang="en">
<head>
<meta charset="utf-8">
<title>Brightfield Dental – Letterhead and Envelope</title>
<link href="https://fonts.googleapis.com/css2?family=Alegreya:wght@400;700&display=swap" rel="stylesheet">
<style>
  :root {
    --canvas: #ffffff;
    --paper: #ffffff;
    --ink: #111111;
    --green: #45b14a;
    --green-soft: rgba(69, 177, 74, .55);
    --green-fade: rgba(69, 177, 74, 0);
    --window: #555555;
  }
  * { margin: 0; padding: 0; box-sizing: border-box; }
  html, body { width: 969px; height: 1200px; overflow: hidden; background: var(--canvas); }
  body { position: relative; font-family: "Alegreya", Georgia, serif; color: var(--ink); }

  .letterhead {
    position: absolute; left: 60px; top: 53px; width: 856px; height: 1103px;
    background: var(--paper); box-shadow: 0 0 4px rgba(0,0,0,.25);
  }
  .recipient, .reference {
    position: absolute; top: 44px; font-size: 18px; line-height: 23px; text-transform: uppercase;
  }
  .recipient { left: 41px; }
  .reference { left: 660px; }
  .reference .date { margin-top: 23px; }
  .salutation { position: absolute; left: 41px; top: 175px; font-size: 18px; }

  .sender { position: absolute; left: 55px; top: 860px; font-size: 18px; line-height: 23px; text-transform: uppercase; }
  .sender .name { font-weight: 700; }
  .sender .phone { margin-top: 23px; font-weight: 700; letter-spacing: .3px; }
  .sender .phone span { margin-left: 12px; }

  .brand-mark {
    position: absolute; display: flex; align-items: center; justify-content: center; text-align: center;
    border: 2px solid var(--green); border-radius: 50%;
    color: var(--green); font-weight: 700; text-transform: uppercase; letter-spacing: 3px; line-height: 1.3;
  }
  .letterhead .brand-mark { left: 664px; top: 872px; width: 144px; height: 144px; font-size: 15px; }

  .leaf-art {
    position: absolute; border-radius: 45%;
    background: radial-gradient(ellipse at center, var(--green-soft) 0%, var(--green-fade) 72%);
  }
  .letterhead .leaf-art { left: 325px; top: 755px; width: 330px; height: 300px; }

  .wave-band {
    position: absolute; left: 0; right: 0; bottom: 0;
    background: linear-gradient(to bottom, var(--green-fade) 0%, var(--green-soft) 100%);
  }
  .letterhead .wave-band { height: 70px; }

  .envelope {
    position: absolute; left: 26px; top: 424px; width: 840px; height: 364px;
    background: var(--paper); box-shadow: 0 0 4px rgba(0,0,0,.3);
    transform-origin: 0 0; transform: rotate(-7.4deg);
  }
  .return-address { position: absolute; left: 33px; top: 24px; font-size: 13px; line-height: 17px; text-transform: uppercase; }
  .return-address .name { font-weight: 700; }
  .address-window {
    position: absolute; left: 80px; top: 205px; width: 358px; height: 105px;
    border: 1.5px solid var(--window);
  }
  .envelope .brand-mark { left: 690px; top: 171px; width: 124px; height: 124px; font-size: 13px; letter-spacing: 2.5px; }
  .envelope .leaf-art { left: 440px; top: 40px; width: 240px; height: 250px; }
  .envelope .wave-band { height: 55px; }
</style>
</head>
<body>
  <section class="letterhead" aria-label="Letterhead">
    <div class="recipient">
      <p>Client Name</p>
      <p>Client Address</p>
      <p>State</p>
    </div>
    <div class="reference">
      <p>Client Account</p>
      <p>Client Ref</p>
      <p class="date">Date</p>
    </div>
    <p class="salutation">Dear Mrs Client,</p>

    <div class="leaf-art" role="img" aria-label="Illustration of two green leaves on a stem"></div>

    <div class="sender">
      <p class="name">Brightfield Dental</p>
      <p>4820 Aspen Ridge Rd</p>
      <p>Suite 210 Westminster</p>
      <p>CO 80031</p>
      <p class="phone">Call<span>720-555-0142</span></p>
    </div>
    <div class="brand-mark">Brightfield<br>Dental</div>

    <div class="wave-band" role="img" aria-label="Decorative green wave ornament"></div>
  </section>

  <section class="envelope" aria-label="Envelope number 10">
    <div class="return-address">
      <p class="name">Brightfield Dental</p>
      <p>4820 Aspen Ridge Rd</p>
      <p>Suite 210 Westminster</p>
      <p>CO 80031</p>
    </div>
    <div class="address-window" aria-label="Address window"></div>
    <div class="leaf-art" role="img" aria-label="Illustration of two green leaves on a stem"></div>
    <div class="brand-mark">Brightfield<br>Dental</div>
    <div class="wave-band" role="img" aria-label="Decorative green wave ornament"></div>
  </section>
</body>
</html>
```